Quillmoor Farm Organic Flower Farm, Farmer Florist

I am a flower grower and florist, so I do everything from the field to the vase. I want to include my website, phone, email and instagram

```html
<!DOCTYPE html>
<html lang="en">
<head>
<meta charset="utf-8">
<title>Quillmoor – Business Card</title>
<link rel="stylesheet" href="https://fonts.googleapis.com/css2?family=Gilda+Display&family=Montserrat:wght@400;500&display=swap">
<style>
  :root {
    --blush: #f2eef0;
    --paper: #ffffff;
    --sage: #9ccc9f;
    --sage-soft: #b9dcbb;
    --plum: #5c2b31;
    --plum-icon: #5e2e33;
    --white: #ffffff;
  }
  html, body {
    margin: 0;
    padding: 0;
    overflow: hidden;
    background: var(--blush);
  }
  .card {
    position: relative;
    width: 1200px;
    height: 686px;
    overflow: hidden;
    background: var(--blush);
  }
  .card-shape {
    position: absolute;
    inset: 0;
  }
  .identity {
    position: absolute;
    left: 36px;
    top: 224px;
    width: 590px;
    text-align: center;
  }
  .identity-name {
    margin: 0;
    font-family: "Gilda Display", "Times New Roman", serif;
    font-weight: 400;
    font-size: 84px;
    line-height: 1;
    letter-spacing: 4px;
    color: var(--plum);
  }
  .identity-role {
    margin: 16px 0 0;
    font-family: "Montserrat", Arial, sans-serif;
    font-weight: 400;
    font-size: 27px;
    line-height: 1;
    letter-spacing: 2px;
    color: var(--sage);
  }
  .floral-sprig {
    position: absolute;
    left: 0;
    top: 380px;
    width: 470px;
    height: 190px;
    border-radius: 0 120px 90px 0 / 0 95px 95px 0;
    background: linear-gradient(100deg, var(--sage) 0%, var(--sage-soft) 70%, rgba(185, 220, 187, 0.35) 100%);
  }
  .contact-list {
    position: absolute;
    left: 731px;
    top: 163px;
    margin: 0;
    padding: 0;
    list-style: none;
  }
  .contact-item {
    display: flex;
    align-items: center;
    height: 64px;
    margin-bottom: 34px;
    font-family: "Montserrat", Arial, sans-serif;
    font-weight: 500;
    font-size: 24px;
    color: var(--plum);
    white-space: nowrap;
  }
  .contact-icon {
    flex: none;
    width: 64px;
    height: 64px;
    border-radius: 50%;
    background: var(--plum-icon);
    margin-right: 21px;
    display: flex;
    align-items: center;
    justify-content: center;
  }
  .contact-icon svg {
    width: 32px;
    height: 32px;
  }
  .contact-icon-handle {
    font-family: "Montserrat", Arial, sans-serif;
    font-weight: 500;
    font-size: 32px;
    line-height: 1;
    color: var(--white);
    margin-top: -4px;
  }
</style>
</head>
<body>
  <main class="card">
    <svg class="card-shape" width="1200" height="686" viewBox="0 0 1200 686" aria-hidden="true">
      <circle cx="51" cy="343" r="614" fill="var(--paper)"/>
      <path d="M553 -6 A617 617 0 0 1 617 560" fill="none" stroke="var(--sage)" stroke-width="7" stroke-linecap="round"/>
    </svg>

    <header class="identity">
      <h1 class="identity-name">QUILLMOOR</h1>
      <p class="identity-role">FARMER FLORIST</p>
    </header>

    <div class="floral-sprig" role="img" aria-label="Sage green botanical sprig of wildflowers and leaves"></div>

    <ul class="contact-list">
      <li class="contact-item">
        <span class="contact-icon">
          <svg viewBox="0 0 24 24" aria-hidden="true"><path fill="#fff" d="M6.6 10.8a15.1 15.1 0 0 0 6.6 6.6l2.2-2.2c.3-.3.7-.4 1-.2 1.1.4 2.3.6 3.6.6.6 0 1 .4 1 1V20c0 .6-.4 1-1 1A17 17 0 0 1 3 4c0-.6.4-1 1-1h3.5c.6 0 1 .4 1 1 0 1.3.2 2.5.6 3.6.1.3 0 .7-.2 1z"/></svg>
        </span>
        (708) 5550 2817
      </li>
      <li class="contact-item">
        <span class="contact-icon">
          <svg viewBox="0 0 24 24" aria-hidden="true"><rect x="2.5" y="5" width="19" height="14" rx="1" fill="#fff"/><path d="M3 6l9 7 9-7" fill="none" stroke="var(--plum-icon)" stroke-width="1.6"/></svg>
        </span>
        hello@quillmoorfarm.com.au
      </li>
      <li class="contact-item">
        <span class="contact-icon">
          <svg viewBox="0 0 24 24" aria-hidden="true" fill="none" stroke="#fff" stroke-width="1.6"><circle cx="12" cy="12" r="9"/><ellipse cx="12" cy="12" rx="4" ry="9"/><path d="M3 12h18M4.5 7.5h15M4.5 16.5h15"/></svg>
        </span>
        www.quillmoor.com
      </li>
      <li class="contact-item">
        <span class="contact-icon"><span class="contact-icon-handle" aria-hidden="true">@</span></span>
        quillmooronthegram
      </li>
    </ul>
  </main>
</body>
</html>
```